Chocoloate confectionery company requires vibrant Packaging Design for a mini chocolate bar

- Need a packaging design for a new product; a chocolate mini-bar.
- Our corporate colors of brown and pink should be included in design.
- The chocolate weighs 20grams and measures 8 cm length x 5 cm width x 1 cm depth
- It will be covered in gold foil and wrapped in a paper sleeve.
- The paper sleeve measures 13.5 cm length x 7.5 cm width
- The paper sleeve can then be sectioned into 3 equal areas
- The packaging design is required on middle section of the sleeve.
- The ingredients, company details, barcode and disclaimer etc will be on the right section
- The left section of the sleeve may be left blank

PLEASE SEE SAMPLE PICTURES PER ATTACHED

Target Market(s)

Everyday shoppers (e.g. Moms, Dads, kids, teens, students)

Industry/Entity Type

It Company

Requirements
Must have
• Brown and pink colors (as per business card attached)
Name of mini chocolate bar is Mallow Nib. This must appear on middle section of paper sleeve

```html
<!DOCTYPE html>
<html lang="en">
<head>
<meta charset="utf-8">
<title>Mallow Nib – Mini Bar Sleeve</title>
<link rel="stylesheet" href="https://fonts.googleapis.com/css2?family=Alegreya:wght@400;700&family=Arimo:ital@0;1&family=Didact+Gothic&display=swap">
<style>
  :root {
    --paper: #ffffff;
    --cocoa-dark: #3d2116;
    --cocoa: #5a3424;
    --cocoa-mid: #8a6a5c;
    --latte: #cbbcb3;
    --cream: #f3efec;
    --pink: #e23a9b;
    --pink-soft: #f06ab8;
    --ink: #111111;
  }
  * { margin: 0; padding: 0; box-sizing: border-box; }
  html, body { width: 667px; height: 1200px; overflow: hidden; background: var(--paper); }
  .sleeve { position: relative; width: 667px; height: 1200px; background: var(--paper); }

  .front-panel {
    position: absolute; left: 0; top: 380px; width: 667px; height: 372px;
    background: linear-gradient(100deg, var(--cocoa-mid) 0%, var(--latte) 35%, var(--cream) 70%, #ffffff 100%);
    overflow: hidden;
  }
  .front-panel svg { position: absolute; left: 0; top: 0; }

  .brand-name {
    position: absolute; left: 62px; top: 40px;
    font-family: "Alegreya", serif; font-weight: 700; font-size: 76px;
    letter-spacing: 3px; color: var(--cocoa-dark); line-height: 1;
  }
  .tagline {
    position: absolute; left: 186px; top: 162px;
    font-family: "Alegreya", serif; font-size: 30px; color: var(--pink); line-height: 1;
  }
  .weight {
    position: absolute; left: 15px; top: 322px;
    font-family: "Alegreya", serif; font-size: 32px; color: var(--cocoa); line-height: 1;
  }

  .info { position: absolute; left: 10px; top: 762px; width: 650px; color: var(--ink); }
  .info-row { font-family: "Didact Gothic", sans-serif; font-size: 16px; line-height: 27px; }
  .info-label { font-family: "Arimo", sans-serif; font-size: 25px; }
  .origin {
    position: absolute; left: 162px; top: 882px;
    font-family: "Arimo", sans-serif; font-style: italic; font-size: 24px; color: var(--ink);
  }
</style>
</head>
<body>
<main class="sleeve">
  <section class="front-panel">
    <svg width="667" height="372" viewBox="0 0 667 372">
      <defs>
        <radialGradient id="swirlTone" cx="0.62" cy="0.45" r="0.7">
          <stop offset="0" stop-color="#2a140c"/>
          <stop offset="0.4" stop-color="#7a4a34"/>
          <stop offset="0.75" stop-color="#4a2718"/>
          <stop offset="1" stop-color="#2e170e"/>
        </radialGradient>
        <linearGradient id="curlTone" x1="0" y1="0" x2="1" y2="1">
          <stop offset="0" stop-color="#ffffff"/>
          <stop offset="1" stop-color="#d9ccc5"/>
        </linearGradient>
      </defs>
      <path class="chocolate-swirl" role="img" aria-label="Swirl of melted chocolate"
            d="M667 80 C600 150 470 260 345 372 L667 372 Z" fill="url(#swirlTone)"/>
      <path class="page-curl" d="M492 0 L667 0 L667 80 C600 110 540 95 505 60 C490 40 488 20 492 0 Z" fill="url(#curlTone)"/>
      <ellipse class="lips-top" role="img" aria-label="Pink lips kiss mark" cx="555" cy="70" rx="68" ry="50" fill="var(--pink-soft)"/>
      <ellipse class="lips-left" role="img" aria-label="Pink lips kiss mark" cx="130" cy="205" rx="50" ry="48" fill="var(--pink)"/>
    </svg>
    <h1 class="brand-name">MALLOW NIB</h1>
    <p class="tagline">HOMEMADE CHOCOLATE</p>
    <p class="weight">20g</p>
  </section>

  <section class="info">
    <p class="info-row"><span class="info-label">Ingredients:</span> Sugar,Soya,hydrogenated vegetable fats(Palm Kernel),<br>Malted ext rin,Low fat,Cocoa powder,Whop powder(Milk),Lecithin,<br>Favouring,Emulsifier</p>
    <p class="info-row"><span class="info-label">Allergins:</span> Contains cows milk,Soya beans,Mey contain tree nuts</p>
  </section>
  <p class="origin">Homemade in Zimbabwe</p>
</main>
</body>
</html>
```